6 - 8 'Holistic' Instagram Graphics

Hi there!
We are looking to build up a library of Graphic Templates to use as Instagram & Facebook posts for our Holistic Medi Spa (& 3 other companies eventually)
This competition is for a sample of 6 - 8 designs. For the winner(s), we will make an agreement for a batch order (Looking for 200+ designs in total), and will be looking to make a long term arrangement.
Please find a full job description in the attached Word Document.
Any questions, don't hesitate to ask.
Thanks!
Medical Spa

```html
<!DOCTYPE html>
<html lang="en">
<head>
<meta charset="utf-8">
<title>Willowmere Holistic Medi Spa – Social Post Set</title>
<link href="https://fonts.googleapis.com/css2?family=Jost:wght@300;400;600&display=swap" rel="stylesheet">
<style>
  :root{
    --stage:#f3d9c3;
    --white:#ffffff;
    --ink:#857f72;
    --mist:#e3f2f2;
    --mist-soft:#eef7f8;
    --sand:#f8ebe0;
    --sand-line:#e6cfae;
    --coral:#f08a72;
    --dot-grey:#f1f1f1;
  }
  *{box-sizing:border-box;margin:0;padding:0}
  html,body{width:1200px;height:1200px;overflow:hidden;background:var(--stage)}
  body{position:relative;font-family:"Jost",sans-serif;color:var(--ink)}

  .post{position:absolute;background:var(--white);overflow:hidden}
  .post--square{left:48px;top:286px;width:353px;height:353px}
  .post--story{left:421px;top:286px;width:354px;height:628px}
  .post--offer{left:799px;top:286px;width:353px;height:625px}

  .layer{position:absolute;inset:0}
  .brand{position:absolute;display:flex;align-items:center;gap:4px;color:var(--ink)}
  .brand__mark{width:9px;height:9px;border-radius:50%;background:var(--mist);border:1px solid var(--ink)}
  .brand__text{display:flex;flex-direction:column;line-height:1}
  .brand__name{font-weight:400;font-size:11px;letter-spacing:.1px}
  .brand__tag{font-weight:400;font-size:3.6px;letter-spacing:.6px;margin-top:1px}

  /* square post */
  .skin-photo{position:absolute;left:107px;top:11px;width:239px;height:239px;
    border-radius:26px 70px 36px 170px / 26px 70px 36px 170px;
    background:linear-gradient(135deg,#e9c4ae 0%,#dcab93 45%,#c89a86 70%,#5b4136 100%)}
  .quote{position:absolute;left:22px;top:222px;font-weight:300;font-size:21.5px;line-height:25.5px;letter-spacing:.2px;text-transform:uppercase}
  .post--square .brand{left:280px;top:330px}

  /* story post */
  .post--story .brand{left:263px;top:31px}
  .mantra-box{position:absolute;left:96px;top:400px;width:162px;height:181px;border-radius:14px;
    background:var(--white);border:4px solid var(--mist-soft)}
  .mantra{position:absolute;left:17px;top:12px;font-weight:300;font-size:20.5px;line-height:25.3px;text-transform:uppercase;white-space:nowrap}
  .mantra strong{font-weight:600}

  /* offer post */
  .dots{position:absolute;display:grid;gap:0}
  .dots--coral{left:26px;top:18px;grid-template-columns:repeat(4,15px);grid-auto-rows:20.5px}
  .dots--coral span{width:3px;height:3px;border-radius:50%;background:var(--coral)}
  .dots--grey{left:22px;top:518px;grid-template-columns:repeat(4,16px);grid-auto-rows:15px}
  .dots--grey span{width:8px;height:8px;border-radius:50%;background:var(--dot-grey)}
  .offer-sand{position:absolute;left:116px;top:36px;width:237px;height:337px;background:var(--sand)}
  .device-photo{position:absolute;left:0;top:121px;width:250px;height:312px;
    background:linear-gradient(150deg,#f1ece8 0%,#e7dcd3 40%,#d9a58a 70%,#c9a7d8 100%)}
  .offer-box{position:absolute;left:75px;top:373px;width:203px;height:154px;background:var(--mist-soft);text-align:center}
  .offer{font-weight:600;font-size:40px;line-height:46px;padding-top:26px;letter-spacing:-.3px}
  .brand--vertical{left:255px;top:190px;transform:rotate(-90deg);transform-origin:left top;top:305px;left:279px}
  .brand--vertical .brand__name{font-size:24px;font-weight:300}
  .brand--vertical .brand__tag{font-size:7.5px;letter-spacing:1.3px;margin-top:2px}
  .brand--vertical .brand__mark{width:16px;height:16px;margin-right:4px}
</style>
</head>
<body>

<!-- Post 1: square quote -->
<section class="post post--square">
  <svg class="layer" viewBox="0 0 353 353" aria-hidden="true">
    <path d="M0 0 H93 C92 40 95 80 90 120 C85 145 60 150 30 148 C15 147 5 145 0 145 Z" fill="var(--mist)"/>
    <path d="M92 0 C60 20 58 60 55 100 C52 130 40 150 0 150" fill="none" stroke="var(--sand-line)" stroke-width="1"/>
    <path d="M160 353 C180 320 220 290 280 280 C320 275 345 260 353 245 V353 Z" fill="var(--sand)"/>
    <path d="M130 353 C140 300 180 280 240 282 C300 285 340 270 353 200" fill="none" stroke="var(--sand-line)" stroke-width="1"/>
    <path d="M220 262 C250 250 290 250 310 240 C330 230 345 215 353 200 V260 C330 270 280 272 220 262 Z" fill="#f7f9fa"/>
  </svg>
  <div class="skin-photo" role="img" aria-label="Close-up photo of a woman's cheek and lips during a facial cupping treatment"></div>
  <p class="quote">A healthy<br>outside starts<br>from the<br>inside.</p>
  <div class="brand">
    <span class="brand__mark"></span>
    <span class="brand__text"><span class="brand__name">Willowmere</span><span class="brand__tag">HOLISTIC MEDI SPA</span></span>
  </div>
</section>

<!-- Post 2: story mantra -->
<section class="post post--story">
  <svg class="layer" viewBox="0 0 354 628" aria-hidden="true">
    <path d="M210 0 H354 V145 C330 150 305 140 290 110 C275 80 250 75 225 72 C205 70 195 40 210 0 Z" fill="var(--sand)"/>
    <path d="M0 420 C40 410 70 450 85 500 C100 540 170 560 185 600 L175 628 H0 Z" fill="var(--mist-soft)"/>
    <circle cx="95" cy="13" r="3" fill="var(--mist)"/>
    <circle cx="340" cy="228" r="2" fill="var(--mist)"/>
    <circle cx="283" cy="565" r="2.5" fill="var(--mist)"/>
    <circle cx="290" cy="470" r="1.8" fill="#f3d3c3"/>
    <circle cx="300" cy="478" r="1.5" fill="#f3d3c3"/>
  </svg>
  <svg class="layer" viewBox="0 0 354 628" role="img" aria-label="Photo of a red-haired woman meditating cross-legged outdoors">
    <defs>
      <linearGradient id="meditationTones" x1="0" y1="0" x2="1" y2="1">
        <stop offset="0" stop-color="#eef2f4"/>
        <stop offset=".45" stop-color="#d9dde6"/>
        <stop offset=".7" stop-color="#c7b6c9"/>
        <stop offset="1" stop-color="#b9a7c6"/>
      </linearGradient>
    </defs>
    <path d="M95 12 C60 20 25 90 22 175 C20 250 60 320 130 350 C190 370 255 358 300 330 C345 300 352 240 340 200 C330 160 300 140 262 135 C215 128 180 60 150 30 C130 12 112 8 95 12 Z" fill="url(#meditationTones)"/>
  </svg>
  <div class="brand">
    <span class="brand__mark"></span>
    <span class="brand__text"><span class="brand__name">Willowmere</span><span class="brand__tag">HOLISTIC MEDI SPA</span></span>
  </div>
  <div class="mantra-box">
    <p class="mantra"><strong>Health</strong> is<br>a state<br>of body.<br><strong>Wellness</strong> is<br>a state<br>of being.</p>
  </div>
</section>

<!-- Post 3: offer -->
<section class="post post--offer">
  <div class="dots dots--coral">
    <span></span><span></span><span></span><span></span>
    <span></span><span></span><span></span><span></span>
    <span></span><span></span><span></span><span></span>
    <span></span><span></span><span></span><span></span>
    <span></span><span></span><span></span><span></span>
  </div>
  <div class="offer-sand"></div>
  <div class="device-photo" role="img" aria-label="Photo of a gloved therapist using a body contouring device on a client's abdomen"></div>
  <div class="brand brand--vertical">
    <span class="brand__mark"></span>
    <span class="brand__text"><span class="brand__name">Willowmere</span><span class="brand__tag">HOLISTIC MEDI SPA</span></span>
  </div>
  <div class="offer-box">
    <p class="offer">SAVE<br>20 - 25%</p>
  </div>
  <div class="dots dots--grey">
    <span></span><span></span><span></span><span></span>
    <span></span><span></span><span></span><span></span>
    <span></span><span></span><span></span><span></span>
    <span></span><span></span><span></span><span></span>
    <span></span><span></span><span></span><span></span>
    <span></span><span></span><span></span><span></span>
    <span></span><span></span><span></span><span></span>
  </div>
</section>

</body>
</html>
```